Oral Surgery Office Referral Forms and Stationary Designs

I want something like the ones you made for Harbor Crest Oral Surgery. Please use my logo for color scheme and refer to this URL:

https://www.plornexa.example/design/552031

I would also like similar business cards with appointment date/time as well as stationaries.

Target Market(s)

Referring dentists

Industry/Entity Type

Office

Font styles to use
Serif

Requirements
Must have
• same as harbor crest oral surgery forms, I will add or delete items as I find fit once the design is ready

```html
<!DOCTYPE html>
<html lang="en">
<head>
<meta charset="utf-8">
<title>Dr. Varlen – Business Cards</title>
<link href="https://fonts.googleapis.com/css2?family=Lato:wght@300;400;700&display=swap" rel="stylesheet">
<style>
  :root{
    --bg:#1c1c1c;
    --card-white:#ffffff;
    --card-dark:#3b3b3b;
    --card-dark-2:#2f2f2f;
    --green:#2bd38a;
    --ink:#333333;
    --muted:#9a9a9a;
    --line:#555555;
  }
  *{margin:0;padding:0;box-sizing:border-box}
  html,body{width:1200px;height:896px;overflow:hidden;background:var(--bg);font-family:"Lato",sans-serif}
  .canvas{position:relative;width:1200px;height:896px}
  .card{position:absolute;top:293px;width:540px;height:310px;border-radius:18px;overflow:hidden}

  /* appointment card */
  .appointment{left:40px;background:var(--card-white);color:var(--ink)}
  .appointment .title{position:absolute;left:30px;top:26px;font-size:22px;font-weight:400}
  .field{position:absolute;left:30px;display:flex;align-items:flex-end;font-size:12px}
  .field .label{white-space:nowrap;margin-right:6px}
  .field .rule{border-bottom:1px solid var(--ink);height:14px;position:relative}
  .field .hint{position:absolute;bottom:3px;font-size:8px;color:var(--muted)}
  .box{display:inline-block;width:10px;height:10px;border:1px solid var(--green);vertical-align:middle;margin-right:4px}
  .ampm{position:absolute;left:206px;top:133px;font-size:11px;white-space:nowrap}
  .ampm span{margin-right:12px}
  .days{position:absolute;left:340px;top:28px;font-size:11px}
  .days .row{display:flex;gap:12px;margin-bottom:8px}
  .days .row span{min-width:52px}
  .comments-label{position:absolute;left:340px;top:120px;font-size:11px}
  .comments{position:absolute;left:340px;top:138px;width:170px;height:110px;border:1px solid var(--ink)}

  /* front card */
  .front{left:620px;background:linear-gradient(135deg,var(--card-dark),var(--card-dark-2));color:#fff}
  .front .role{position:absolute;right:40px;top:28px;text-align:right}
  .front .role .name{font-size:22px;font-weight:700}
  .front .role .title{font-size:13px;font-weight:300}
  .front .role-line{position:absolute;left:30px;top:88px}
  .front .brand{position:absolute;left:30px;top:110px;display:flex;align-items:center;gap:14px}
  .front .brand .dot{width:34px;height:34px;border-radius:50%;background:var(--green)}
  .front .brand .name{font-size:34px;font-weight:300;line-height:1;letter-spacing:1px}
  .front .brand .sub{font-size:16px;font-weight:300;margin-top:4px}
  .contacts{position:absolute;left:30px;top:178px;font-size:12px;font-weight:400;list-style:none}
  .contacts li{display:flex;align-items:center;gap:8px;margin-bottom:4px}
  .contacts svg{width:11px;height:11px}
  .band{position:absolute;left:0;right:0;bottom:0;height:34px;background:var(--green);border-top:3px solid #e8e8e8;display:flex;align-items:center;gap:8px;padding-left:22px;font-size:13px;color:#fff}
</style>
</head>
<body>
<div class="canvas">

  <section class="card appointment">
    <h2 class="title">Your's Next Appointment:</h2>

    <div class="field" style="top:72px"><span class="label">Today's Date:</span>
      <span class="rule" style="width:200px"><span class="hint" style="left:30px">DD</span><span class="hint" style="left:90px">MM</span><span class="hint" style="left:150px">YYYY</span></span></div>
    <div class="field" style="top:102px"><span class="label">Appt. Date:</span>
      <span class="rule" style="width:210px"><span class="hint" style="left:30px">DD</span><span class="hint" style="left:90px">MM</span><span class="hint" style="left:150px">YYYY</span></span></div>
    <div class="field" style="top:132px"><span class="label">Time:</span><span class="rule" style="width:130px"></span></div>
    <div class="ampm"><span><i class="box"></i>AM</span><span><i class="box"></i>PM</span></div>
    <div class="field" style="top:162px"><span class="label">Patient's Name:</span><span class="rule" style="width:200px"></span></div>
    <div class="field" style="top:192px"><span class="label">Patient's Phone Number:</span><span class="rule" style="width:150px"></span></div>
    <div class="field" style="top:222px"><span class="label">Referred By:</span><span class="rule" style="width:220px"></span></div>

    <div class="days">
      <div class="row"><span>Day:</span><span><i class="box"></i>Mon</span><span><i class="box"></i>Tus</span></div>
      <div class="row"><span></span><span><i class="box"></i>Wed</span><span><i class="box"></i>Thurs</span></div>
      <div class="row"><span></span><span><i class="box"></i>Fri</span><span><i class="box"></i>Sat</span></div>
      <div class="row"><span></span><span><i class="box"></i>Sun</span></div>
    </div>
    <div class="comments-label">Additional Comments:</div>
    <div class="comments"></div>
  </section>

  <section class="card front">
    <div class="role">
      <div class="name">Dr. Varlen</div>
      <div class="title">CEO/Founder</div>
    </div>
    <svg class="role-line" width="480" height="20" viewBox="0 0 480 20">
      <line x1="0" y1="10" x2="260" y2="10" stroke="#cfcfcf" stroke-width="1"/>
      <line x1="260" y1="10" x2="470" y2="10" stroke="var(--green)" stroke-width="2"/>
      <circle cx="472" cy="10" r="3.5" fill="var(--green)"/>
    </svg>

    <div class="brand">
      <span class="dot"></span>
      <div>
        <div class="name">DR. VARLEN</div>
        <div class="sub">Oral Surgeon</div>
      </div>
    </div>

    <ul class="contacts">
      <li><svg viewBox="0 0 12 12"><circle cx="6" cy="6" r="5.5" fill="var(--green)"/><path d="M4 3.5l1 1-0.6.8a4 4 0 0 0 2.3 2.3l.8-.6 1 1-.8.8C5.8 8.6 3.4 6.2 3.2 4.3z" fill="#fff"/></svg>: +49 555-010-2040</li>
      <li><svg viewBox="0 0 12 12"><rect x="1" y="4" width="10" height="5" rx="1" fill="var(--green)"/><rect x="3" y="1.5" width="6" height="3" fill="var(--green)"/><rect x="3" y="7.5" width="6" height="3" fill="#fff"/></svg>: +49 555-010-2041</li>
      <li><svg viewBox="0 0 12 12"><rect x="0.5" y="2.5" width="11" height="7" fill="var(--green)"/><path d="M0.5 2.5l5.5 4 5.5-4" stroke="#fff" fill="none"/></svg>: info@drvarlen.example</li>
      <li><svg viewBox="0 0 12 12"><circle cx="6" cy="6" r="5.5" fill="var(--green)"/><path d="M0.5 6h11M6 0.5v11M2 3h8M2 9h8" stroke="#fff" stroke-width="0.7"/></svg>: www.drvarlen.example</li>
    </ul>

    <div class="band">
      <svg width="10" height="13" viewBox="0 0 10 13"><path d="M5 0a4.5 4.5 0 0 0-4.5 4.5C.5 8 5 13 5 13s4.5-5 4.5-8.5A4.5 4.5 0 0 0 5 0z" fill="#333"/><circle cx="5" cy="4.5" r="1.6" fill="var(--green)"/></svg>
      <span>: Dr. Varlen, Lindenweg 14, 50999 Musterstadt</span>
    </div>
  </section>

</div>
</body>
</html>
```